Postcard Design

Kelvaro is a medical sales and communication network between doctors and doctors, doctors and sales representatives and doctors and medical companies. Doctors offices are off limits to sales reps. Communication takes place on a closed network of computer tablets. Doctors,Companies and Sale Representatives must join the the Kelvaro network and then they begin to send short videos or messages or pdf files to those doctors in their territory. Doctors will post the Kel varo logo on their doors, restricting sales reps from waiting in offices to make cold calls. They receive permission for office visits
through the tablet based platform.

Industry/Entity Type

Communication

```html
<!DOCTYPE html>
<html lang="en">
<head>
<meta charset="utf-8">
<title>Kelvaro – Sales Representative Restricted Office Postcard</title>
<link rel="stylesheet" href="https://fonts.googleapis.com/css2?family=Open+Sans:wght@300;400;600;700&display=swap">
<style>
  :root {
    --page-bg: #e9ebee;
    --card-white: #ffffff;
    --blue-light: #2f7fae;
    --blue-mid: #1d5f8c;
    --blue-deep: #0f3d63;
    --navy: #0b2a4a;
    --navy-band: #0a2747;
    --ring: rgba(20, 70, 110, 0.75);
    --text-white: #ffffff;
    --text-soft: #cfe6f5;
    --accent: #5fb6e6;
  }
  * { margin: 0; padding: 0; box-sizing: border-box; }
  html, body {
    width: 1200px; height: 976px; overflow: hidden;
    background: var(--page-bg);
    font-family: "Open Sans", Arial, sans-serif;
  }
  .postcard {
    position: absolute; left: 40px; top: 89px;
    width: 1120px; height: 798px;
    background: var(--card-white);
    overflow: hidden;
    box-shadow: 0 6px 24px rgba(0,0,0,0.18);
  }
  .postcard__shapes { position: absolute; inset: 0; }
  .brand-box {
    position: absolute; left: 527px; top: 69px;
    width: 559px; height: 132px;
    background: var(--navy);
    display: flex; align-items: center; gap: 18px;
    padding: 0 30px;
  }
  .brand-box__mark {
    width: 70px; height: 70px; border-radius: 50%;
    background: var(--accent); flex: none;
  }
  .brand-box__name {
    font-size: 52px; font-weight: 700; letter-spacing: 1px;
    color: var(--accent); line-height: 1;
  }
  .brand-box__tagline {
    font-size: 18px; font-weight: 600; color: var(--accent);
    margin-top: 6px;
  }
  .headline {
    position: absolute; right: 29px; top: 303px;
    text-align: right; color: var(--text-white);
    font-weight: 300; font-size: 52px; line-height: 56px;
    letter-spacing: 0.5px;
  }
  .instructions {
    position: absolute; left: 610px; top: 508px; width: 478px;
    border-top: 2px solid var(--text-white);
    border-bottom: 2px solid var(--text-white);
    padding: 13px 0 10px;
    text-align: right; color: var(--text-white);
    font-weight: 700; font-size: 21px; line-height: 29px;
  }
  .web-band {
    position: absolute; left: 0; top: 706px; width: 1120px; height: 70px;
    background: var(--navy-band);
  }
  .web-band__url {
    position: absolute; right: 95px; top: 10px;
    color: var(--text-white); font-weight: 700; font-size: 38px;
    letter-spacing: 11px; line-height: 50px;
  }
</style>
</head>
<body>
  <main class="postcard">
    <svg class="postcard__shapes" width="1120" height="798" viewBox="0 0 1120 798">
      <defs>
        <linearGradient id="panelGradient" x1="0" y1="0" x2="0.3" y2="1">
          <stop offset="0" stop-color="#3a8dbb"/>
          <stop offset="0.45" stop-color="#1f6593"/>
          <stop offset="1" stop-color="#0f3d63"/>
        </linearGradient>
        <radialGradient id="photoGradient" cx="0.55" cy="0.5" r="0.6">
          <stop offset="0" stop-color="#eef2f5"/>
          <stop offset="0.55" stop-color="#c9d3dc"/>
          <stop offset="1" stop-color="#b08a78"/>
        </radialGradient>
      </defs>
      <!-- blue panel with curved top edge -->
      <path class="blue-panel" d="M0 44 H440 C480 44 495 22 540 22 H1120 V776 H0 Z" fill="url(#panelGradient)"/>
      <!-- ring around photo -->
      <circle class="photo-ring" cx="285" cy="410" r="293" fill="var(--ring)"/>
      <circle class="photo-ring-inner" cx="285" cy="410" r="262" fill="#1b5a86"/>
      <!-- photo area -->
      <circle class="photo" cx="285" cy="410" r="249" fill="url(#photoGradient)"
        role="img" aria-label="Photo of a hand holding a stethoscope shaped like a clock in front of a doctor's white coat"/>
    </svg>

    <div class="brand-box">
      <span class="brand-box__mark"></span>
      <div>
        <div class="brand-box__name">KELVARO</div>
        <div class="brand-box__tagline">Leaders in Healthcare Communication</div>
      </div>
    </div>

    <h1 class="headline">SALES REPRESENTATIVE<br>RESTRICTIED OFFICE</h1>

    <p class="instructions">PICK UP SALE REPRESENTATIVE PACKET<br>AT FRONT DESK OR SIGN UP AT</p>

    <div class="web-band">
      <span class="web-band__url">www.kelvaro.com</span>
    </div>
  </main>
</body>
</html>
```